I am looking for business cards and letterhead

I want a high-level look for CEO's who want a concierge level leadership consultant and organization development strategist

This needs to go with my brand: simple, elegant, clean. Please improve on this design while using these fonts and colors

Here is my website: CorinneHalvers.com

```html
<!DOCTYPE html>
<html lang="en">
<head>
<meta charset="utf-8">
<title>Corinne Halvers – Stationery Set 4</title>
<link href="https://fonts.googleapis.com/css2?family=Josefin+Sans:wght@400;600;700&family=Source+Sans+3:wght@400&display=swap" rel="stylesheet">
<style>
:root{
  --navy:#0b1438;
  --navy-deep:#020414;
  --ink:#000000;
  --gold:#c9a25e;
  --white:#ffffff;
  --paper:#ffffff;
  --stage-light:#e9e9df;
  --stage-dark:#1e2326;
  --label-dark:#5b6470;
  --label-light:#ffffff;
  --faint:#eef1f5;
}
*{box-sizing:border-box;margin:0;padding:0}
html,body{width:945px;height:1200px;overflow:hidden}
body{position:relative;font-family:"Josefin Sans",sans-serif;background:var(--stage-dark)}
.stage-top{position:absolute;left:0;top:0;width:945px;height:532px;background:var(--stage-light)}
.stage-bottom{position:absolute;left:0;top:532px;width:945px;height:668px;background:var(--stage-dark)}
.label{position:absolute;font-family:"Source Sans 3",sans-serif;font-size:18px}
.label.on-light{color:var(--label-dark)}
.label.on-dark{color:var(--label-light)}

.card{position:absolute;width:380px;height:217px;overflow:hidden;box-shadow:0 8px 22px rgba(0,0,0,.25)}
.card-front{left:75px;top:160px;background:var(--navy)}
.card-back{left:490px;top:160px}
.portrait{position:absolute;right:0;top:0;width:160px;height:130px;background:linear-gradient(160deg,#3a2a24,#1a2347 60%,#0b1438)}
.contact-band{position:absolute;left:128px;top:128px;width:252px;height:72px;background:var(--ink)}
.brand{position:absolute;display:flex;align-items:center;gap:8px;color:var(--gold);font-weight:600}
.brand .dot{border-radius:50%;border:2px solid var(--gold);flex:none}
.card-front .brand{left:18px;top:92px;font-size:11px}
.card-front .brand .dot{width:22px;height:22px}
.card-name{position:absolute;left:136px;top:86px;color:var(--gold);font-weight:700;font-size:14px;letter-spacing:.5px}
.card-cred{position:absolute;left:136px;top:106px;color:var(--white);font-size:10px;letter-spacing:.5px}
.contact-list{list-style:none;color:var(--white)}
.contact-list li{display:flex;align-items:center;justify-content:flex-end;gap:5px;white-space:nowrap}
.contact-list svg{flex:none}
.card-front .contact-list{position:absolute;right:12px;top:136px;font-size:9.5px;line-height:15px}
.scene-photo{position:absolute;inset:0;background:linear-gradient(135deg,#3f5a22,#8a7a4c 45%,#6b8a2c 70%,#2f4a1a)}
.card-back .brand{right:22px;top:90px;color:var(--white);font-size:11px}
.card-back .brand .dot{width:22px;height:22px;border-color:var(--white)}

.sheet{position:absolute;background:var(--paper);overflow:hidden}
.letterhead{left:77px;top:613px;width:375px;height:484px}
.lh-band{position:absolute;left:0;top:7px;width:375px;height:83px;background:var(--navy)}
.lh-band-inner{position:absolute;left:60px;top:9px;width:315px;height:65px;background:var(--navy-deep)}
.lh-seal{position:absolute;left:0;top:0;width:78px;height:83px;background:var(--navy);border-radius:0 42px 42px 0}
.letterhead .brand{left:12px;top:34px;font-size:10px}
.letterhead .brand .dot{width:18px;height:18px}
.letterhead .contact-list{position:absolute;right:14px;top:23px;font-size:7px;line-height:10.3px}
.watermark{position:absolute;color:var(--faint);font-weight:600;text-align:center}
.letterhead .watermark{left:0;width:375px;top:240px;font-size:34px}

.env-front{left:503px;top:614px;width:384px;height:167px}
.env-band{position:absolute;left:0;top:11px;width:384px;height:43px;background:var(--navy)}
.env-band-inner{position:absolute;left:40px;top:5px;width:344px;height:33px;background:var(--navy-deep)}
.env-front .brand{left:10px;top:24px;font-size:8px}
.env-front .brand .dot{width:14px;height:14px}
.env-address{position:absolute;left:71px;top:30px;color:var(--white);font-size:6.5px}
.env-front .watermark{right:14px;top:100px;font-size:24px}

.env-back{left:503px;top:930px;width:384px;height:167px}
.env-flap{position:absolute;left:0;top:0}
.env-back .brand{left:0;width:384px;justify-content:center;top:28px;font-size:9px}
.env-back .brand .dot{width:14px;height:14px}
</style>
</head>
<body>
<div class="stage-top"></div>
<div class="stage-bottom"></div>

<p class="label on-light" style="left:77px;top:56px">Business card_4</p>

<section class="card card-front">
  <div class="portrait" role="img" aria-label="Portrait photo of the consultant in a navy blazer, arms crossed"></div>
  <div class="brand"><span class="dot"></span>Corinne Halvers</div>
  <div class="card-name">CORINNE HALVERS</div>
  <div class="card-cred">MA / ABS</div>
  <div class="contact-band"></div>
  <ul class="contact-list">
    <li>300-200-9000 <svg width="8" height="9" viewBox="0 0 8 9"><rect x="1.5" y=".5" width="5" height="8" rx="1" fill="none" stroke="#c9a25e"/></svg></li>
    <li>info@corinnehalvers.com <svg width="9" height="7" viewBox="0 0 9 7"><rect x=".5" y=".5" width="8" height="6" fill="none" stroke="#c9a25e"/><path d="M.5 .5 4.5 4 8.5 .5" fill="none" stroke="#c9a25e"/></svg></li>
    <li>www.corinnehalvers.com <svg width="9" height="9" viewBox="0 0 9 9"><circle cx="4.5" cy="4.5" r="4" fill="none" stroke="#c9a25e"/><path d="M.5 4.5h8M4.5 .5v8" stroke="#c9a25e"/></svg></li>
    <li>00 dummy city, dummy place 0000 <svg width="7" height="9" viewBox="0 0 7 9"><path d="M3.5 9C1 5.5 0 4.5 0 3.2a3.5 3.5 0 0 1 7 0C7 4.5 6 5.5 3.5 9z" fill="#c9a25e"/><circle cx="3.5" cy="3.2" r="1.2" fill="#000"/></svg></li>
  </ul>
</section>

<section class="card card-back">
  <div class="scene-photo" role="img" aria-label="Photo of a wooded home with a garden deck and patio umbrellas"></div>
  <div class="brand"><span class="dot"></span>Corinne Halvers</div>
</section>

<p class="label on-dark" style="left:77px;top:576px">Letterhead_4</p>
<section class="sheet letterhead">
  <div class="lh-band"><div class="lh-band-inner"></div><div class="lh-seal"></div></div>
  <div class="brand"><span class="dot"></span>Corinne Halvers</div>
  <ul class="contact-list">
    <li>300-200-9000 <svg width="6" height="7" viewBox="0 0 8 9"><rect x="1.5" y=".5" width="5" height="8" rx="1" fill="none" stroke="#c9a25e"/></svg></li>
    <li>info@corinnehalvers.com <svg width="7" height="6" viewBox="0 0 9 7"><rect x=".5" y=".5" width="8" height="6" fill="#c9a25e"/><path d="M.5 .5 4.5 4 8.5 .5" fill="none" stroke="#020414"/></svg></li>
    <li>www.corinnehalvers.com <svg width="7" height="7" viewBox="0 0 9 9"><circle cx="4.5" cy="4.5" r="4" fill="none" stroke="#c9a25e"/><path d="M.5 4.5h8M4.5 .5v8" stroke="#c9a25e"/></svg></li>
    <li>00 dummy city, dummy place 0000 <svg width="6" height="7" viewBox="0 0 7 9"><path d="M3.5 9C1 5.5 0 4.5 0 3.2a3.5 3.5 0 0 1 7 0C7 4.5 6 5.5 3.5 9z" fill="#c9a25e"/></svg></li>
  </ul>
  <div class="watermark">Corinne Halvers</div>
</section>

<p class="label on-dark" style="left:503px;top:576px">ENV Front_4</p>
<section class="sheet env-front">
  <div class="env-band"><div class="env-band-inner"></div></div>
  <div class="brand"><span class="dot"></span></div>
  <div class="env-address">00 dummy city, dummy place 0000</div>
  <div class="watermark">Corinne Halvers</div>
</section>

<p class="label on-dark" style="left:503px;top:892px">ENV Back_4</p>
<section class="sheet env-back">
  <svg class="env-flap" width="384" height="62" viewBox="0 0 384 62">
    <path d="M0 0H384C378 14 372 32 350 36L200 60Q192 62 184 60L34 36C12 32 6 14 0 0Z" fill="#0b1438"/>
  </svg>
  <div class="brand"><span class="dot"></span></div>
</section>
</body>
</html>
```